Upgrade 4 Images - Bid 1, then we can discuss the other 3

We have a four graphics that we use in various presentations and business proposals. We want to upgrade them to make them really pop and match the level of service we provide, without going overboard.

We're open to new ideas, but the general form and content should stay the same.

I'd like to have all four designed by the same person, but I'm assuming this bid will be for 1 of the four, and then the other three can be contracted as additions.

```html
<!DOCTYPE html>
<html lang="en">
<head>
<meta charset="utf-8">
<title>Operating Quadrants – Data Processing as a Service</title>
<link rel="stylesheet" href="https://fonts.googleapis.com/css2?family=Raleway:wght@500;600;700;800&family=Roboto+Condensed:ital,wght@1,800&family=Montserrat:wght@900&display=swap">
<style>
  :root {
    --page: #ffffff;
    --sheet: #cbe1de;
    --sheet-light: #d6e8e6;
    --header-start: #c8e0dd;
    --header-end: #ebf4f5;
    --title-blue: #0a5bb5;
    --accent-orange: #fa852e;
    --segment-blue: #207ed8;
    --segment-orange: #fb852d;
    --core: #eaf4f2;
    --halo: #e6f2f0;
    --ink: #111111;
    --logo-panel: #eaf2f2;
  }
  * { margin: 0; padding: 0; box-sizing: border-box; }
  html, body {
    width: 1200px; height: 1200px; overflow: hidden;
    background: var(--page);
  }
  .canvas { position: relative; width: 1200px; height: 1200px; }
  .poster {
    position: absolute; left: 234px; top: 52px; width: 732px; height: 1096px;
    background: linear-gradient(160deg, var(--sheet-light), var(--sheet) 60%, var(--sheet-light));
    overflow: hidden;
  }
  .poster-header {
    position: absolute; left: 0; top: 0; width: 100%; height: 131px;
    background: linear-gradient(90deg, var(--header-start) 0%, var(--header-start) 40%, var(--header-end) 100%);
    text-align: center;
  }
  .poster-title {
    position: absolute; left: 0; right: 0; top: 29px;
    font-family: "Raleway", sans-serif; font-weight: 800;
    font-size: 45px; line-height: 1; letter-spacing: 0.5px;
    color: var(--title-blue);
  }
  .poster-subtitle {
    position: absolute; left: 0; right: 0; top: 77px;
    font-family: "Raleway", sans-serif; font-weight: 700;
    font-size: 28px; line-height: 1;
    color: var(--accent-orange);
  }
  .quadrant-diagram { position: absolute; left: 0; top: 0; width: 1200px; height: 1200px; }
  .segment-label {
    font-family: "Raleway", sans-serif; font-weight: 700;
    font-size: 40px; fill: #ffffff; letter-spacing: 1px;
  }
  .axis-label {
    font-family: "Roboto Condensed", sans-serif; font-style: italic; font-weight: 800;
    font-size: 25px; fill: var(--ink);
    stroke: #ffffff; stroke-width: 5px; paint-order: stroke; stroke-linejoin: round;
  }
  .zone-label {
    font-family: "Montserrat", sans-serif; font-weight: 900;
    font-size: 34px; fill: var(--ink);
  }
  .brand-panel {
    position: absolute; left: 17px; top: 953px; width: 269px; height: 84px;
    background: var(--logo-panel);
    display: flex; align-items: center; justify-content: center;
  }
  .brand-name {
    font-family: "Raleway", sans-serif; font-weight: 600;
    font-size: 27px; color: var(--accent-orange); white-space: nowrap;
  }
  .web-address {
    position: absolute; right: 13px; top: 1028px;
    font-family: "Raleway", sans-serif; font-weight: 500;
    font-size: 21px; color: var(--ink);
  }
  .footer-rule {
    position: absolute; left: 0; top: 1052px; width: 100%; height: 3px;
    background: var(--accent-orange);
  }
  .footer-band {
    position: absolute; left: 0; top: 1060px; width: 100%; height: 36px;
    background: var(--accent-orange);
  }
</style>
</head>
<body>
<div class="canvas">
  <div class="poster">
    <header class="poster-header">
      <h1 class="poster-title">OPERATING QUADRANTS</h1>
      <p class="poster-subtitle">–Data Processing as a Service–</p>
    </header>

    <div class="brand-panel">
      <span class="brand-name">The Kelvane Group</span>
    </div>
    <p class="web-address">www.kelvanegroup.com</p>
    <div class="footer-rule"></div>
    <div class="footer-band"></div>
  </div>

  <svg class="quadrant-diagram" viewBox="0 0 1200 1200" aria-labelledby="diagram-title">
    <title id="diagram-title">Operating quadrants: maturity versus utilization</title>
    <defs>
      <path id="arc-top-left" d="M400,578 A200,200 0 0 1 600,378"/>
      <path id="arc-top-right" d="M600,378 A200,200 0 0 1 800,578"/>
      <path id="arc-bottom-left" d="M370,578 A230,230 0 0 0 600,808"/>
      <path id="arc-bottom-right" d="M600,808 A230,230 0 0 0 830,578"/>
    </defs>

    <circle class="ring-halo" cx="600" cy="578" r="267" fill="var(--halo)"/>
    <circle class="ring-core" cx="600" cy="578" r="170" fill="var(--core)"/>

    <g class="segments">
      <path class="segment segment-specialist" fill="var(--segment-orange)"
            d="M581.5,318.66 A260,260 0 0 0 340.66,559.5 L431.01,559.5 A170,170 0 0 1 581.5,409.01 Z"/>
      <path class="segment segment-enterprise" fill="var(--segment-blue)"
            d="M618.5,318.66 A260,260 0 0 1 859.34,559.5 L768.99,559.5 A170,170 0 0 0 618.5,409.01 Z"/>
      <path class="segment segment-adhoc" fill="var(--segment-blue)"
            d="M581.5,837.34 A260,260 0 0 1 340.66,596.5 L431.01,596.5 A170,170 0 0 0 581.5,746.99 Z"/>
      <path class="segment segment-factory" fill="var(--segment-orange)"
            d="M618.5,837.34 A260,260 0 0 0 859.34,596.5 L768.99,596.5 A170,170 0 0 1 618.5,746.99 Z"/>
    </g>

    <g class="segment-outlines" fill="none" stroke="var(--ink)" stroke-width="5">
      <path d="M581.5,318.66 A260,260 0 0 0 340.66,559.5"/>
      <path d="M431.01,559.5 A170,170 0 0 1 581.5,409.01"/>
      <path d="M618.5,318.66 A260,260 0 0 1 859.34,559.5"/>
      <path d="M768.99,559.5 A170,170 0 0 0 618.5,409.01"/>
      <path d="M581.5,837.34 A260,260 0 0 1 340.66,596.5"/>
      <path d="M431.01,596.5 A170,170 0 0 0 581.5,746.99"/>
      <path d="M618.5,837.34 A260,260 0 0 0 859.34,596.5"/>
      <path d="M768.99,596.5 A170,170 0 0 1 618.5,746.99"/>
    </g>

    <g class="segment-labels">
      <text class="segment-label"><textPath href="#arc-top-left" startOffset="50%" text-anchor="middle">SPECIALIST</textPath></text>
      <text class="segment-label"><textPath href="#arc-top-right" startOffset="50%" text-anchor="middle">ENTERPRISE</textPath></text>
      <text class="segment-label"><textPath href="#arc-bottom-left" startOffset="50%" text-anchor="middle">AD HOC</textPath></text>
      <text class="segment-label"><textPath href="#arc-bottom-right" startOffset="50%" text-anchor="middle">FACTORY</textPath></text>
    </g>

    <g class="axis-labels">
      <text class="axis-label" transform="translate(609,351) rotate(-90)" text-anchor="middle">High Maturity</text>
      <text class="axis-label" transform="translate(609,807) rotate(-90)" text-anchor="middle">Low Maturity</text>
      <text class="axis-label" x="380" y="587" text-anchor="middle">Low Utilization</text>
      <text class="axis-label" x="821" y="585" text-anchor="middle">High Utilization</text>
    </g>

    <g class="zone">
      <text class="zone-label" x="600" y="569" text-anchor="middle">GOLDILOCKS</text>
      <text class="zone-label" x="600" y="616" text-anchor="middle">ZONE</text>
    </g>
  </svg>
</div>
</body>
</html>
```